Business Card design for new private practice opening

I need a business card design for my new private practice with my new logo uploaded as a file
On the front the logo
On the back: maybe a small logo somewhere?
Priv. Doz. DDr. Petra Sommerfeld
Fachärztin für Allgemein- & Viszeralchirurgie
Address: xxx
Tel: xxx
Mobil:xxx
Webseite:xxx
Email:xxx

Contact Information for Business Card

See project description above for details

Requirements
Nice to have
• I would like the colors of the logo incorporated into the business card

```html
<!DOCTYPE html>
<html lang="de">
<head>
<meta charset="utf-8">
<title>Lindenhof Chirurgie – Visitenkarte</title>
<link rel="stylesheet" href="https://fonts.googleapis.com/css2?family=Open+Sans:wght@400;600;700&display=swap">
<style>
  :root {
    --teal: #3dbdb6;
    --teal-dark: #2fa69f;
    --slate: #6d6e6d;
    --slate-text: #6f7070;
    --paper: #ffffff;
    --ground: #eceeed;
    --faint: rgba(255, 255, 255, 0.08);
  }
  * { box-sizing: border-box; margin: 0; padding: 0; }
  html, body {
    width: 1200px; height: 800px; overflow: hidden;
    background: var(--ground);
    font-family: "Open Sans", Arial, sans-serif;
  }
  .sheet {
    width: 1200px; height: 800px;
    display: flex; align-items: center; justify-content: center; gap: 40px;
  }
  .card {
    position: relative;
    width: 540px; height: 309px;
    border: 9px solid var(--teal);
    overflow: hidden;
    box-shadow: 0 6px 18px rgba(0, 0, 0, 0.12);
  }

  /* Front */
  .card--front {
    background: var(--paper);
    display: flex; flex-direction: column; align-items: center; justify-content: center;
  }
  .brand { display: flex; align-items: center; gap: 14px; }
  .brand__dot {
    width: 66px; height: 66px; border-radius: 50%;
    background: var(--teal); flex-shrink: 0;
  }
  .brand__name {
    font-weight: 700; font-size: 30px; line-height: 1;
    letter-spacing: 1px; text-transform: uppercase;
    color: var(--slate-text);
  }
  .front__rule {
    width: 300px; height: 1px; background: var(--slate-text);
    margin: 18px 0 12px;
  }
  .front__web {
    font-size: 12px; letter-spacing: 3px; font-weight: 600;
    color: var(--slate-text);
  }
  .front__web .domain { color: var(--teal); }

  /* Back */
  .card--back {
    background: var(--slate);
    color: var(--paper);
    padding: 22px 26px;
  }
  .back__mark {
    position: absolute; right: -40px; bottom: -60px;
    width: 230px; height: 230px; border-radius: 50%;
    background: var(--faint);
    border: 4px solid rgba(255, 255, 255, 0.12);
  }
  .card--back .brand__dot { width: 50px; height: 50px; }
  .card--back .brand__name { color: var(--paper); font-size: 22px; }
  .doctor { margin-top: 14px; }
  .doctor__name { color: var(--teal); font-weight: 600; font-size: 14px; }
  .doctor__role { font-size: 11.5px; margin-top: 1px; }
  .contacts { list-style: none; margin-top: 10px; font-size: 11.5px; }
  .contacts li { display: flex; align-items: center; gap: 8px; line-height: 1.55; }
  .contacts svg { width: 11px; height: 11px; flex-shrink: 0; }
  .back__rule { width: 230px; height: 1px; background: var(--teal); margin: 8px 0 6px; }
  .address { font-size: 11.5px; }
</style>
</head>
<body>
<main class="sheet">
  <section class="card card--front" aria-label="Vorderseite">
    <div class="brand">
      <span class="brand__dot"></span>
      <span class="brand__name">Lindenhof<br>Chirurgie</span>
    </div>
    <div class="front__rule"></div>
    <p class="front__web">www.<span class="domain">lindenhofchirurgie</span>.com</p>
  </section>

  <section class="card card--back" aria-label="Rückseite">
    <div class="back__mark"></div>
    <div class="brand">
      <span class="brand__dot"></span>
      <span class="brand__name">Lindenhof<br>Chirurgie</span>
    </div>
    <div class="doctor">
      <p class="doctor__name">Priv. Doz. DDr. Petra Sommerfeld</p>
      <p class="doctor__role">Fachärztin für Allgemein- &amp; Viszeralchirurgie</p>
    </div>
    <ul class="contacts">
      <li>
        <svg viewBox="0 0 12 12" aria-hidden="true"><rect x="3" y="0.5" width="6" height="11" rx="1" fill="none" stroke="#3dbdb6"/><line x1="5" y1="9.5" x2="7" y2="9.5" stroke="#3dbdb6"/></svg>
        XXX-XXX-XXXX
      </li>
      <li>
        <svg viewBox="0 0 12 12" aria-hidden="true"><rect x="0.5" y="2" width="11" height="8" fill="none" stroke="#3dbdb6"/><polyline points="0.5,2 6,7 11.5,2" fill="none" stroke="#3dbdb6"/></svg>
        info@lindenhofchirurgie.com
      </li>
      <li>
        <svg viewBox="0 0 12 12" aria-hidden="true"><path d="M2 1 L4.5 1 L5.5 3.5 L4 4.5 Q5 7 7.5 8 L8.5 6.5 L11 7.5 L11 10 Q6 11 1 3 Z" fill="#3dbdb6"/></svg>
        300-555-0142
      </li>
      <li>
        <svg viewBox="0 0 12 12" aria-hidden="true"><circle cx="6" cy="6" r="5.3" fill="none" stroke="#3dbdb6"/><ellipse cx="6" cy="6" rx="2.3" ry="5.3" fill="none" stroke="#3dbdb6"/><line x1="0.7" y1="6" x2="11.3" y2="6" stroke="#3dbdb6"/></svg>
        www.lindenhofchirurgie.com
      </li>
    </ul>
    <div class="back__rule"></div>
    <p class="address">00 dummy city, dummy place 0000</p>
  </section>
</main>
</body>
</html>
```